Website for courses for men for making money, health, fitness

I require a website which is going to be a mix of a crypto currency website and website aimed at providing men with money making, health, relationship advice courses and content

The name isn't decided yet so for now please call it something like

VANTAGE DEN

A platform dedicated to making men wealthy, physically strong, mentally tough & successful with women

In the top right, I need it to show how many points they have, they must buy points in order to use them to claim the courses.

WHAT WE DO

Vantage den is a platform where you can learn everything you need about business, making money, crypto currency, fitness, health, mental toughness and resilience and how to be successful with women all in one place

HOW WILL THIS WORK & WHY SHOULD I BUY POINTS?

xxxxxxxxxxxxxxxxxxxxxxxx
xxxxxxxxxxxxxxxxxxxxxxx
xxxxxxxxxxxxxxxxxxxxx

AFFILIATE SCHEME

EARN UP TO $125 DOLLARS PER PERSON WHO SIGNS UP THROUGH YOUR LINK

START EARNING NOW - button
______________________________________________________

BUY POINTS
(A maximum of only $250 worth of points can be purchased per person until the platform goes fully live)

ROAD MAP & THE MODEL

2023

Q1 - PRE BUY IN FOR POINTS

Q2 - FULL WEBSITE LAUNCH

Q3 - APP LAUNCH

Q4 - IN APP ADVERT LAUNCH

It must have a very slick and sharp eye catching look, and be designed to convert people into purchasing points

some ideas of the feel of the website -

https://brelvora.io/
https://plimwick.style/
https://fable.korvell.com/

```html
<!DOCTYPE html>
<html lang="en">
<head>
<meta charset="utf-8">
<title>Vantage Den</title>
<link href="https://fonts.googleapis.com/css2?family=Saira+Condensed:wght@700;800&family=Nunito+Sans:wght@300;400;600;700&display=swap" rel="stylesheet">
<style>
:root{
  --navy:#1c3562;
  --navy-deep:#152a50;
  --band:#3e5d89;
  --heading:#3b5a86;
  --cyan:#dff8fb;
  --text:#3a3f4a;
  --white:#ffffff;
}
*{margin:0;padding:0;box-sizing:border-box}
html,body{width:1200px;height:3440px;overflow:hidden;background:var(--white)}
body{position:relative;font-family:"Nunito Sans",sans-serif;color:var(--text)}
.abs{position:absolute}
.display{font-family:"Saira Condensed",sans-serif;font-weight:800;letter-spacing:-0.3px}
.placeholder{position:absolute;border-radius:14px}

/* hero */
.hero{position:absolute;left:0;top:0;width:1200px;height:640px}
.logo{left:147px;top:36px;font-size:32px;color:var(--white)}
.nav a{position:absolute;top:50px;font-size:15px;color:var(--white);text-decoration:none}
.nav .active{border-bottom:2px solid var(--white);padding-bottom:2px}
.points-pill{left:890px;top:44px;width:110px;height:36px;border-radius:18px;background:var(--cyan);color:var(--navy);font-size:14px;display:flex;align-items:center;justify-content:center}
.hero-welcome{left:152px;top:262px;font-size:34px;color:var(--white)}
.hero-title{left:150px;top:296px;font-size:68px;color:var(--white);line-height:1}
.btn{position:absolute;display:flex;align-items:center;justify-content:center;font-size:16px;border-radius:3px;text-decoration:none}
.btn-light{background:var(--cyan);color:var(--navy)}
.btn-dark{background:var(--band);color:var(--white)}

/* sections */
.section-title{font-size:32px;color:var(--heading)}
.body-copy{font-size:17.5px;line-height:27px;text-align:justify;color:var(--text)}
.band{position:absolute;left:0;top:1032px;width:1200px;height:222px;background:var(--band);color:var(--white);text-align:center}
.affiliate{position:absolute;left:0;top:1683px;width:1200px;height:427px;background:linear-gradient(120deg,#2d4b78,#3e5d89 50%,#34527f);overflow:hidden}
.earn-box{left:143px;top:1790px;width:915px;height:205px;border:3px solid #dbe6f3;border-radius:12px;background:rgba(255,255,255,.12);text-align:center;color:var(--white)}

/* roadmap */
.step-card{position:absolute;width:208px;height:183px;background:var(--band);border-radius:12px;color:var(--white);text-align:center;padding:0 8px}
.step-card h3{font-size:19px;font-weight:700;line-height:25px;margin-bottom:2px;white-space:nowrap}
.step-card p{font-size:14px;line-height:21px;color:#dfe7f2;white-space:nowrap}
.step-dot{position:absolute;width:90px;height:90px;border-radius:50%;background:var(--cyan);color:var(--band);font-size:30px;font-weight:700;display:flex;align-items:center;justify-content:center}

/* buy */
.buy{position:absolute;left:0;top:2750px;width:1200px;height:323px;background:var(--band)}
.buy-text{left:519px;top:2850px;font-size:26px;line-height:37px;color:var(--white);font-weight:300;width:560px}

/* footer */
.footer-nav{position:absolute;left:5px;top:3125px;width:1195px;height:40px;background:var(--cyan)}
.footer-nav a{position:absolute;top:10px;font-size:16px;color:var(--text);text-decoration:none}
.foot-small{font-size:14px;line-height:25px;color:var(--text)}
.foot-contact{font-size:16px;color:var(--text)}
.vline{position:absolute;width:1px;background:#999}
</style>
</head>
<body>

<!-- hero -->
<svg class="hero" viewBox="0 0 1200 640" aria-hidden="true">
  <defs>
    <linearGradient id="heroGrad" x1="0" y1="0" x2="1" y2="1">
      <stop offset="0" stop-color="#1f3a68"/>
      <stop offset="1" stop-color="#16305a"/>
    </linearGradient>
  </defs>
  <path d="M0 0H1200V585C1100 565 1000 560 860 580C700 603 560 630 400 632C220 634 100 625 0 617Z" fill="url(#heroGrad)"/>
  <path d="M0 240C150 180 300 230 615 160V280C400 320 200 280 0 340Z" fill="#24436f" opacity=".45"/>
</svg>
<div class="abs logo display">Vantage Den</div>
<nav class="nav">
  <a class="active" style="left:437px">Home</a>
  <a style="left:524px">What We Do</a>
  <a style="left:653px">Who We Are</a>
  <a style="left:781px">Buy Points</a>
</nav>
<div class="abs points-pill">Points : 4592</div>
<svg class="abs" style="left:1030px;top:50px" width="22" height="22" viewBox="0 0 22 22" aria-hidden="true"><circle cx="9" cy="9" r="7" fill="none" stroke="#fff" stroke-width="2"/><path d="M14 14l6 6" stroke="#fff" stroke-width="2"/></svg>
<div class="abs hero-welcome display">Welcome to</div>
<div class="abs hero-title display">Vantage Den</div>
<a class="btn btn-light" style="left:147px;top:395px;width:161px;height:40px">Get Started</a>
<div class="placeholder" role="img" aria-label="Illustration of a smartphone with banking screens, coins and security shields" style="left:650px;top:150px;width:485px;height:330px;background:radial-gradient(ellipse at center,#3f6a9e 0%,#23426f 60%,rgba(31,58,104,0) 80%)"></div>

<!-- what we do -->
<div class="abs section-title display" style="left:147px;top:738px">WHAT WE DO</div>
<p class="abs body-copy" style="left:147px;top:794px;width:578px">Vantage den is a platform where you can learn everything you need about business, making money, crypto currency, fitness, health, mental toughness and resilience and how to be successful with women all in one place.</p>
<div class="placeholder" role="img" aria-label="Photo of men training on treadmills in a gym" style="left:782px;top:683px;width:197px;height:124px;background:linear-gradient(135deg,#8a8f96,#c9cdd2)"></div>
<div class="placeholder" role="img" aria-label="Photo of a woman celebrating against a sunset sky" style="left:952px;top:713px;width:173px;height:110px;background:linear-gradient(135deg,#f3b45a,#d9782f 60%,#5a3a2a)"></div>
<div class="placeholder" role="img" aria-label="Photo of a business meeting with documents on a desk" style="left:816px;top:823px;width:244px;height:112px;background:linear-gradient(135deg,#c7c9cc,#3b3f46)"></div>

<!-- band -->
<div class="band">
  <div class="display" style="position:absolute;left:0;width:1200px;top:36px;font-size:32px">VANTAGE DEN</div>
  <div style="position:absolute;left:0;width:1200px;top:97px;font-size:21px;font-weight:300">A platform dedicated to making men</div>
  <div style="position:absolute;left:0;width:1200px;top:130px;font-size:28px;font-weight:700">Physically Strong | &nbsp;Mentally Tough | Successful With Women</div>
</div>

<!-- how -->
<div class="abs section-title display" style="left:0;width:1240px;text-align:center;top:1322px">HOW WILL THIS WORK &amp; WHY SHOULD I BUY POINTS?</div>
<div class="placeholder" role="img" aria-label="Photo of a hand passing cash across a desk with a laptop" style="left:150px;top:1405px;width:313px;height:197px;background:linear-gradient(135deg,#4a4d52,#8b8e92 60%,#5d5650)"></div>
<p class="abs body-copy" style="left:492px;top:1425px;width:585px;font-size:16px;line-height:27px">Lorem ipsum dolor sit amet, consectetur adipiscing elit, sed do eiusmod tempor incididunt ut labore et dolore magna aliqua. Quis ipsum suspendisse ultrices gravida. Risus commodo viverra maecenas accumsan lacus vel facilisis. Lorem ipsum dolor sit amet, consectetur adipiscing elit.</p>
<a class="btn btn-dark" style="left:492px;top:1551px;width:161px;height:40px">Read More</a>

<!-- affiliate -->
<div class="affiliate" role="img" aria-label="Faint background image of an affiliate marketing interface with icons"></div>
<div class="abs display" style="left:0;width:1200px;text-align:center;top:1725px;font-size:32px;color:var(--white)">AFFILIATE SCHEME</div>
<div class="abs earn-box">
  <div style="margin-top:42px;font-size:27px;font-weight:300">EARN UP TO</div>
  <div style="font-size:38px;font-weight:700;line-height:40px">$125 DOLLARS</div>
  <div style="margin-top:6px;font-size:27px;font-weight:300">PER PERSON WHO SIGNS UP THROUGH YOUR LINK</div>
</div>
<a class="btn btn-light" style="left:496px;top:2023px;width:208px;height:40px">Start Earning Now</a>

<!-- roadmap -->
<div class="abs section-title display" style="left:0;width:1200px;text-align:center;top:2184px;font-size:34px">ROAD MAP &nbsp;AND THE MODEL (2022)</div>
<div class="abs" style="left:247px;top:2459px;width:703px;height:8px;background:var(--cyan)"></div>
<div class="step-card" style="left:380px;top:2280px;padding-top:16px"><h3>FULL WEBSITE<br>LAUNCH</h3><p>Lorem ipsum dolor sit<br>amet, consectetur<br>adipiscing elit, sed do</p></div>
<div class="step-card" style="left:848px;top:2282px;padding-top:16px"><h3>IN APP ADVERT<br>LAUNCH</h3><p>Lorem ipsum dolor sit<br>amet, consectetur<br>adipiscing elit, sed do</p></div>
<div class="step-card" style="left:146px;top:2470px;padding-top:48px"><h3>PRE BUY IN FOR<br>POINTS</h3><p>Lorem ipsum dolor sit<br>amet, consectetur<br>adipiscing elit, sed do</p></div>
<div class="step-card" style="left:614px;top:2470px;padding-top:52px"><h3>APP LAUNCH</h3><p>Lorem ipsum dolor sit<br>amet, consectetur<br>adipiscing elit, sed do</p></div>
<div class="step-dot" style="left:202px;top:2418px">1</div>
<div class="step-dot" style="left:437px;top:2417px">2</div>
<div class="step-dot" style="left:671px;top:2419px">3</div>
<div class="step-dot" style="left:905px;top:2417px">4</div>

<!-- buy points -->
<div class="abs" style="left:245px;top:2742px;width:710px;height:341px;background:var(--cyan)"></div>
<div class="buy"></div>
<div class="placeholder" role="img" aria-label="Illustration of a red discount card with a gold coin and sparkles" style="left:150px;top:2800px;width:270px;height:220px;background:radial-gradient(circle at 50% 50%,#d8303a 0%,#b8262f 35%,rgba(62,93,137,0) 60%)"></div>
<div class="abs display" style="left:519px;top:2795px;font-size:32px;color:var(--white)">BUY POINTS</div>
<div class="abs buy-text">(A maximum of only <b style="font-weight:700;font-size:29px">$250 worth</b><br>of points can be purchased per person until the platform goes fully live)</div>
<a class="btn btn-light" style="left:519px;top:2998px;width:162px;height:40px">Buy Now</a>

<!-- footer -->
<nav class="footer-nav">
  <a style="left:299px">Home</a>
  <a style="left:398px">What We Do</a>
  <a style="left:546px">Who We Are</a>
  <a style="left:692px">Buy Points</a>
  <a style="left:825px">Contacts</a>
</nav>
<div class="abs display" style="left:145px;top:3196px;font-size:32px;line-height:36px;color:var(--heading)">Vantage<br>Den</div>
<div class="abs foot-small" style="left:372px;top:3208px"><b style="font-weight:700">Help Links</b><br>Support<br>Terms &amp; Conditions<br>Privacy Policy</div>
<div class="vline" style="left:540px;top:3210px;height:100px"></div>
<svg class="abs" style="left:570px;top:3219px" width="12" height="16" viewBox="0 0 12 16" aria-hidden="true"><path d="M6 0a6 6 0 0 0-6 6c0 4 6 10 6 10s6-6 6-10a6 6 0 0 0-6-6zm0 8.5A2.5 2.5 0 1 1 6 3.5a2.5 2.5 0 0 1 0 5z" fill="#333"/></svg>
<div class="abs foot-contact" style="left:596px;top:3216px;line-height:32px">#7, Harlow Lane<br>Brenton City,<br>USA - 60417</div>
<div class="vline" style="left:771px;top:3210px;height:100px"></div>
<svg class="abs" style="left:802px;top:3214px" width="18" height="18" viewBox="0 0 18 18" aria-hidden="true"><path d="M4 1l3 4-2 2c1 2 3 4 5 5l2-2 4 3-2 3C8 16 2 10 1 3z" fill="none" stroke="#333" stroke-width="1.4"/></svg>
<svg class="abs" style="left:802px;top:3255px" width="16" height="12" viewBox="0 0 16 12" aria-hidden="true"><rect width="16" height="12" rx="1" fill="#333"/><path d="M0 1l8 6 8-6" stroke="#fff" fill="none" stroke-width="1.2"/></svg>
<svg class="abs" style="left:802px;top:3290px" width="16" height="16" viewBox="0 0 16 16" aria-hidden="true"><circle cx="8" cy="8" r="7" fill="none" stroke="#333" stroke-width="1.4"/><ellipse cx="8" cy="8" rx="3" ry="7" fill="none" stroke="#333" stroke-width="1.2"/><path d="M1 8h14" stroke="#333" stroke-width="1.2"/></svg>
<div class="abs foot-contact" style="left:830px;top:3216px;line-height:35px">+(1) 555-014-2290<br>info@vantageden.net<br>www.vantageden.net</div>
<div class="abs" style="left:12px;top:3365px;width:1188px;height:1px;background:#aaa"></div>
<div class="abs" style="left:0;width:1200px;text-align:center;top:3385px;font-size:14px;color:var(--text)">© copyrights 2022 &nbsp;Vantage Den | &nbsp;All Rights Reserved</div>

</body>
</html>
```